Health Education Non-Profit Needs a Designer to Layout Magazine (Contest)

Hello, we are looking for someone to layout our print magazine. We'd like to work with someone who also has graphic design experience manipulating photos (see 2 sample issue links below for examples). Ad design is also needed. We like the current design of our magazine, so we are hoping our next designer can maintain the same look and feel as our previous magazines. Samples of our past two issues can be found at https://www.harbolwellness.org/wp-content/uploads/2019/03/issue-09-feb-2019.pdf and https://www.harbolwellness.org/wp-content/uploads/2018/11/the-bright-almanac-2018-05-issue-08.pdf

There are typically 2-4 different issues per year with around 11 articles in each issue. Issues are 24 pages. If there is a lot of white space, we may ask the designer to design an ad at the end of the article. We are looking to work with someone who is responsive and has a quick turnaround time (e.g., takes around 3 weeks to design the entire issue).

For this contest, please design a cover and article. Please refer to our last two issues (links above) before designing. We would like to see how the designer can take the images and edit them in a way that incorporates them seamlessly into the magazine as has been done in the past. Our end goal will be for the designer to design the entire issue and future issues. We anticipate this contest will not cover the entire cost of the work for completing the issue. When we find a designer we like, we will work out details for additional payment. Images can be found here: https://files.quorvanshare.net/folders/7KpTzRwq2LmXvNb4Hs9JdYeCa0FgUi3Q?usp=sharing

```html
<!DOCTYPE html>
<html lang="en">
<head>
<meta charset="utf-8">
<title>Caregiving Together – Article Page</title>
<link rel="stylesheet" href="https://fonts.googleapis.com/css2?family=Open+Sans:ital,wght@0,400;0,700;1,400&display=swap">
<style>
  :root {
    --ink: #231f20;
    --rule-red: #c8202f;
    --deep-green: #1d4a43;
    --paper: #ffffff;
    --photo-warm: #b88a6a;
    --photo-cool: #6f7f92;
    --photo-light: #d9cbbd;
  }
  html, body { margin: 0; padding: 0; overflow: hidden; background: var(--paper); }
  .page {
    position: relative; width: 1000px; height: 1200px; overflow: hidden;
    background: var(--paper); color: var(--ink);
    font-family: "Open Sans", Arial, sans-serif; font-size: 15px; line-height: 18.2px;
  }
  .top-rule { position: absolute; left: 37px; right: 37px; top: 53px; height: 2px; background: var(--rule-red); }
  .col { position: absolute; margin: 0; z-index: 2; }
  .ln { display: block; white-space: nowrap; }
  .subhead { font-weight: 700; margin: 0; }
  .indent { text-indent: 26px; }
  .pull-quote { font-weight: 700; text-align: center; margin: 0; }
  .pull-quote .attrib { font-weight: 400; }
  .feature-photo, .scene-photo { position: absolute; display: block; z-index: 1; }
  .author-box {
    position: absolute; left: 635px; top: 957px; width: 328px; height: 243px;
    background: var(--deep-green); color: #fff; font-style: italic; font-size: 14.5px; line-height: 18.5px;
    box-sizing: border-box; padding: 12px 54px 0 12px; text-align: right;
  }
  .author-box p { margin: 0; }
</style>
</head>
<body>
<div class="page">
  <div class="top-rule"></div>

  <svg class="feature-photo" style="left:296px;top:-12px" width="384" height="384" viewBox="0 0 384 384" role="img" aria-label="Photo: a caregiver serving a bowl of fresh fruit to an older man seated at a table">
    <defs>
      <linearGradient id="circleTone" x1="0" y1="0" x2="1" y2="1">
        <stop offset="0" stop-color="#a98f9c"/>
        <stop offset="0.5" stop-color="#b88a6a"/>
        <stop offset="1" stop-color="#d9cbbd"/>
      </linearGradient>
    </defs>
    <circle cx="192" cy="192" r="187" fill="url(#circleTone)" stroke="#1d4a43" stroke-width="4"/>
  </svg>

  <div class="col" style="left:63px;top:77px;width:275px">
    <span class="ln">these good outcomes. “While</span>
    <span class="ln">being married can provide</span>
    <span class="ln">a source of support and</span>
    <span class="ln">solace when one person</span>
    <span class="ln">has a chronic illness,</span>
    <span class="ln">some couples may have</span>
    <span class="ln">pre-existing patterns</span>
    <span class="ln">and interactions in the</span>
    <span class="ln">relationship that aren’t</span>
    <span class="ln">healthy,” Marsh says.</span>
    <span class="ln">A psychologist or other</span>
    <span class="ln">counselor can help you</span>
    <span class="ln">work toward a healthier, more</span>
    <span class="ln">productive dynamic.</span>
    <span class="ln">&nbsp;</span>
    <span class="ln subhead" style="padding-left:41px">Communication is key</span>
    <span class="ln subhead">(and it’s okay if you need help</span>
    <span class="ln subhead">with it).</span>
    <span class="ln">No matter what your pre-existing</span>
    <span class="ln">relationship is like, you and your</span>
    <span class="ln">caregiver need “open, clear, and</span>
    <span class="ln">quite intimate communication on</span>
    <span class="ln">both sides,” Brandt says. Remember</span>
    <span class="ln">that you’re in it together, especially</span>
    <span class="ln">during times of stress or conflict.</span>
    <span class="ln">&nbsp;</span>
    <span class="ln indent">“If there’s a disagreement, the first</span>
    <span class="ln">thing to do is have a conversation</span>
    <span class="ln">and really listen to each other. Try</span>
    <span class="ln">not to blame,” says Brandt. “Do a lot</span>
    <span class="ln">of listening and reflecting back: ‘If I</span>
    <span class="ln">heard you correctly, this is what I’m</span>
    <span class="ln">hearing, is that right?’ And then, you</span>
    <span class="ln">can problem-solve effectively as a</span>
    <span class="ln">team.”</span>
    <span class="ln">&nbsp;</span>
    <span class="ln indent">If you’re struggling to do this on</span>
    <span class="ln">your own, psychologists, social</span>
    <span class="ln">workers and other mediators can</span>
    <span class="ln">clarify the problem and find a</span>
    <span class="ln">resolution. Your psychologist or</span>
    <span class="ln">social worker may be especially</span>
    <span class="ln" style="padding-left:94px">helpful if disagreement</span>
    <span class="ln" style="padding-left:120px">involves adherence</span>
    <span class="ln" style="padding-left:126px">to your prescribed</span>
    <span class="ln" style="padding-left:130px">treatment regimen,</span>
    <span class="ln" style="padding-left:128px">which is a frequent</span>
    <span class="ln" style="padding-left:127px">source</span>
    <span class="ln" style="padding-left:127px">of</span>
  </div>

  <div class="col" style="left:370px;top:404px;width:262px">
    <span class="ln">conflict among people on dialysis</span>
    <span class="ln">and their loved ones.</span>
    <span class="ln">&nbsp;</span>
    <span class="ln indent">“If noncompliance is an issue, as</span>
    <span class="ln">a psychologist, I want to know the</span>
    <span class="ln">context,” Brandt says. “Aspects of</span>
    <span class="ln">dialysis may be uncomfortable,</span>
    <span class="ln">painful, expensive, inconvenient, or</span>
    <span class="ln">sad, but these things can often be</span>
    <span class="ln">ameliorated. Together, we can all</span>
    <span class="ln">identify the source of the problem,</span>
    <span class="ln">and then find a way to resolve it.”</span>
    <span class="ln">&nbsp;</span>
    <div class="pull-quote">
      <span class="ln" style="padding-left:20px">For caregivers, feeling</span>
      <span class="ln">overwhelmed and having feelings</span>
      <span class="ln">such as guilt or frustration are</span>
      <span class="ln">understandable and normal,</span>
      <span class="ln attrib">says Marsh.</span>
    </div>
    <span class="ln">&nbsp;</span>
    <span class="ln indent">“It’s a big change to take on an</span>
    <span class="ln">unexpected role,” she says. “It can</span>
    <span class="ln">be helpful for them to know it is</span>
    <span class="ln">common for caregivers to feel</span>
    <span class="ln">this way. It can also be helpful to</span>
    <span class="ln">encourage them to have open</span>
    <span class="ln">communication to express these</span>
    <span class="ln">feelings.”</span>
    <span class="ln">&nbsp;</span>
    <span class="ln" style="padding-left:158px">Marsh also</span>
    <span class="ln" style="padding-left:145px">suggests that</span>
    <span class="ln" style="padding-left:150px">caregivers rely</span>
    <span class="ln" style="padding-left:177px">on the</span>
    <span class="ln" style="padding-left:163px">medical</span>
    <span class="ln" style="padding-left:171px">team,</span>
    <span class="ln" style="padding-left:178px">other</span>
  </div>

  <div class="col" style="left:665px;top:77px;width:290px">
    <span class="ln">family members and friends</span>
    <span class="ln" style="padding-left:8px">for support. “If the caregiver</span>
    <span class="ln" style="padding-left:14px">takes sole responsibility for</span>
    <span class="ln" style="padding-left:20px">everything, [he/she will] get</span>
    <span class="ln" style="padding-left:22px">burned out,” she cautions.</span>
    <span class="ln">&nbsp;</span>
    <span class="ln" style="padding-left:36px">Other ways to prevent</span>
    <span class="ln" style="padding-left:20px">caregiver burnout include</span>
    <span class="ln" style="padding-left:12px">active self-care—like eating</span>
    <span class="ln" style="padding-left:8px">well, getting enough sleep</span>
    <span class="ln" style="padding-left:4px">and exercising—and keeping a</span>
    <span class="ln" style="padding-left:1px">consistent schedule, according to</span>
    <span class="ln">Brandt.</span>
    <span class="ln">&nbsp;</span>
    <span class="ln indent">“When your lives are routinized,</span>
    <span class="ln">you know what to expect and there’s</span>
    <span class="ln">less stress of the unknown,” Brandt</span>
    <span class="ln">says. “Remember to make time</span>
    <span class="ln">for yourself—and find reasons to</span>
    <span class="ln">laugh.”</span>
    <span class="ln">&nbsp;</span>
    <span class="ln indent">She also suggests that caregivers</span>
    <span class="ln">learn “as much as possible about the</span>
    <span class="ln">medical situation and what dialysis</span>
    <span class="ln">is like, and write it down so you</span>
    <span class="ln">can refer to it when you’re feeling</span>
    <span class="ln">overwhelmed,” she says.</span>
    <span class="ln">&nbsp;</span>
    <span class="ln subhead" style="padding-left:26px">Your relationship may grow</span>
    <span class="ln subhead">even stronger.</span>
    <span class="ln">You will undoubtedly face both</span>
    <span class="ln">physical and emotional challenges</span>
    <span class="ln">while on dialysis, no matter your</span>
    <span class="ln">prognosis. But patients and</span>
    <span class="ln">caregivers often become deeply</span>
    <span class="ln">bonded, and Brandt and Marsh say</span>
    <span class="ln">that you have the opportunity for</span>
    <span class="ln">growth and even joy through this</span>
    <span class="ln">ordeal.</span>
    <span class="ln">&nbsp;</span>
    <span class="ln indent">“These challenging situations</span>
    <span class="ln">can actually bring people closer</span>
    <span class="ln">together,” says Marsh. “Patients and</span>
    <span class="ln">caregivers may experience a shift in</span>
    <span class="ln">values after both evaluating what’s</span>
    <span class="ln">truly important in their lives, they</span>
    <span class="ln">may prioritize things in a new way</span>
    <span class="ln">together.”</span>
  </div>

  <svg class="scene-photo" style="left:37px;top:780px" width="550" height="420" viewBox="0 0 550 420" role="img" aria-label="Photo: a nurse in blue scrubs taking notes while talking with an older couple seated on a sofa">
    <defs>
      <linearGradient id="sceneTone" x1="0" y1="0" x2="1" y2="0">
        <stop offset="0" stop-color="#6f7f92"/>
        <stop offset="0.45" stop-color="#b88a6a"/>
        <stop offset="1" stop-color="#8a9fbf"/>
      </linearGradient>
    </defs>
    <path d="M0 420 L0 210 L8 100 L43 62 L93 52 L118 80 L132 120 L148 195 L193 190 L253 190 L283 210 L323 220 L363 180 L383 132 L433 120 L466 135 L483 270 L523 280 L543 330 L543 420 Z" fill="url(#sceneTone)"/>
  </svg>

  <aside class="author-box">
    <p>Nora Whitfield is a writer and editor at the Northfield Behavioral Society. This resource was developed jointly by the Northfield Behavioral Society and Harbol Wellness Education Center as part of a partnership to educate dialysis patients and their families on the psychological and emotional aspects of managing kidney disease.</p>
  </aside>
</div>
</body>
</html>
```